Natural Light/Organic/Documentary Photography Business

I like a simple, approachable, feminine, earthy/organic feel. Earth/neutral tones, nothing too loud or obnoxious. I like the watercolor look. I don't want anything too trendy or something I'll get tired of after a couple months. As far as colors, I am much more a fan of cream/taupe/blue/green...not a fan of pink or purple at all.

Target Market(s)

Weddings & Families

Industry/Entity Type

Wedding Photography

Contact Information for Business Card

website, email, phone number

Font styles to use
Other font styles liked:
• Horizontes, Gotham

Colors

Designer to choose colors to be used in the design.

Requirements
Must have
• Website: www.elspethmarlowe.com
• Phone: 412.638.9057
• Email: elspeth@elspethmarlowe.com
Nice to have
• I like the watercolor look but its not necessary. I like simple/earthy tones. Nothing too loud or distracting. Simple & feminine without being too girly. I like an approachable/soft feel.
• Instagram: www.instagram.com/elspethmarlowephotography/
Should not have
• NO loud colors or design or pattern. I do not want a photo of a camera or lens or anything cheesy like that.

```html
<!DOCTYPE html>
<html lang="en">
<head>
<meta charset="utf-8">
<title>Elspeth Marlowe Photography – Business Card</title>
<link rel="stylesheet" href="https://fonts.googleapis.com/css2?family=PT+Sans:wght@400;700&display=swap">
<style>
  :root {
    --backdrop: #ececec;
    --card-white: #ffffff;
    --taupe: #8e8077;
    --taupe-text: #867870;
    --ink: #3f3f3f;
    --rule: #b9b0aa;
    --on-taupe: #ffffff;
  }
  * { box-sizing: border-box; margin: 0; padding: 0; }
  html, body {
    width: 1200px; height: 799px; overflow: hidden;
    background: var(--backdrop);
    font-family: "PT Sans", sans-serif;
  }
  .canvas { position: relative; width: 1200px; height: 799px; }
  .card {
    position: absolute; left: 313px; width: 584px; height: 334px;
  }
  .card--front { top: 51px; background: var(--card-white); box-shadow: 0 0 0 1px #e2e2e2; }
  .card--back { top: 413px; background: var(--taupe); }

  .brand-name {
    position: absolute; white-space: nowrap;
    font-weight: 400; letter-spacing: 0.5px;
  }
  .card--front .brand-name {
    left: 164px; top: 166px; transform: translate(-50%, -50%);
    font-size: 24px; color: var(--taupe-text);
  }
  .divider {
    position: absolute; left: 292px; top: 111px;
    width: 1px; height: 111px; background: var(--rule);
  }
  .holder-name {
    position: absolute; left: 315px; top: 106px;
    font-size: 22px; font-weight: 700; color: var(--taupe-text);
  }
  .contact-list { position: absolute; left: 315px; top: 144px; list-style: none; }
  .contact-list li {
    display: flex; align-items: center; height: 19.3px;
    font-size: 15px; color: var(--ink);
  }
  .contact-list svg { width: 13px; height: 13px; margin-right: 9px; flex: none; fill: var(--ink); }

  .card--back .brand-name {
    left: 50%; top: 166px; transform: translate(-50%, -50%);
    font-size: 40px; color: var(--on-taupe);
  }
  .back-website {
    position: absolute; left: 0; right: 0; top: 277px; text-align: center;
    font-size: 15px; letter-spacing: 3.4px; color: var(--on-taupe);
  }
</style>
</head>
<body>
<main class="canvas">
  <section class="card card--front">
    <span class="brand-name">Elspeth Marlowe</span>
    <span class="divider"></span>
    <h1 class="holder-name">Elspeth Marlowe</h1>
    <ul class="contact-list">
      <li>
        <svg viewBox="0 0 16 16" aria-hidden="true"><path d="M2 5c0-2 3-3 6-3s6 1 6 3v1h-3V5H5v1H2zM4 7h8l2 6H2z"/></svg>
        412.638.9057
      </li>
      <li>
        <svg viewBox="0 0 16 16" aria-hidden="true"><path d="M1 3h14v2L8 9 1 5zM1 7l7 4 7-4v6H1z"/></svg>
        elspeth@elspethmarlowe.com
      </li>
      <li>
        <svg viewBox="0 0 16 16" aria-hidden="true"><circle cx="8" cy="8" r="7"/><path d="M4 5h4l1 2-2 2v3L5 9z" fill="#fff"/></svg>
        www.elspethmarlowe.com
      </li>
      <li>
        <svg viewBox="0 0 16 16" aria-hidden="true"><circle cx="8" cy="8" r="6.5"/></svg>
        elspethmarlowephotography
      </li>
    </ul>
  </section>

  <section class="card card--back">
    <span class="brand-name">Elspeth Marlowe</span>
    <p class="back-website">WWW.ELSPETHMARLOWE.COM</p>
  </section>
</main>
</body>
</html>
```